Managed IT Services Business Card + Stationary
Making Technology Work for Your Business
thank you for all the business card submissionns.
I'd like to note a change in the cellphone number to (916) 555-0173
I will try to review the submissions in more detail this evening.

```html
<!DOCTYPE html>
<html lang="en">
<head>
<meta charset="utf-8">
<title>Aligna Stationery Set</title>
<link href="https://fonts.googleapis.com/css2?family=Montserrat:wght@700;800&family=Open+Sans:wght@400;600;700&display=swap" rel="stylesheet">
<style>
  :root{
    --backdrop:#2c2c2e;
    --paper:#ffffff;
    --brand-red:#d8232a;
    --brand-red-dark:#9e1218;
    --ink:#3a3a3a;
    --ink-soft:#8a8a8a;
    --rule:#cfcfcf;
    --ghost:#f3eeee;
  }
  *{box-sizing:border-box;margin:0;padding:0}
  html,body{width:1200px;height:625px;overflow:hidden;background:var(--backdrop)}
  body{position:relative;font-family:"Open Sans",Arial,sans-serif;color:var(--ink)}

  .brand{display:flex;align-items:center;gap:5px}
  .brand-dot{border-radius:50%;background:var(--brand-red);flex:none}
  .brand-name{font-family:"Montserrat",Arial,sans-serif;font-weight:800;color:var(--brand-red);letter-spacing:.04em;line-height:1}
  .brand-tag{font-size:4px;letter-spacing:.25em;color:var(--ink-soft);text-transform:uppercase;white-space:nowrap}

  /* business cards */
  .card{position:absolute;left:43px;width:173px;height:108px;background:var(--paper);border-radius:6px;overflow:hidden}
  .card-1{top:67px}.card-2{top:197px}.card-3{top:331px}
  .card .brand{position:absolute;left:12px;top:30px;flex-direction:column;align-items:center;gap:3px}
  .card .brand-dot{width:20px;height:20px}
  .card .brand-name{font-size:11px}
  .card-contact{position:absolute;left:90px;top:14px;font-size:4.5px;line-height:1.6;color:var(--ink-soft)}
  .card-contact .person{font-size:6.5px;font-weight:700;color:var(--ink)}
  .card-contact .role{font-size:4.5px;margin-bottom:5px}
  .card-web{position:absolute;left:0;right:0;bottom:8px;text-align:center;font-size:4px;color:var(--ink-soft)}
  .card-band{position:absolute;left:0;right:0;bottom:0;height:4px;background:var(--brand-red)}
  .card-back{position:absolute;left:43px;top:468px;width:173px;height:108px;border-radius:6px;
    background:linear-gradient(160deg,var(--brand-red) 0%,var(--brand-red-dark) 100%)}
  .card-back .brand{position:absolute;left:14px;top:62px}
  .card-back .brand-dot{width:18px;height:18px;background:var(--paper)}
  .card-back .brand-name{font-size:14px;color:var(--paper)}

  /* letterhead */
  .letterhead{position:absolute;left:252px;top:34px;width:413px;height:547px;background:var(--paper)}
  .letterhead .brand{position:absolute;left:22px;top:14px;flex-direction:column;gap:3px}
  .letterhead .brand-dot{width:24px;height:24px}
  .letterhead .brand-name{font-size:13px}
  .letter-address{position:absolute;left:334px;top:18px;font-size:4.5px;line-height:1.7;color:var(--ink-soft)}
  .letter-ghost{position:absolute;left:118px;top:146px;width:120px;height:120px;border-radius:50%;background:var(--ghost)}
  .letter-footer{position:absolute;left:0;right:0;bottom:0;height:22px;background:linear-gradient(var(--rule),#e8e8e8);border-top:3px solid var(--brand-red)}
  .letter-web{position:absolute;left:0;right:0;bottom:7px;text-align:center;font-size:4px;color:var(--ink)}

  /* envelope */
  .envelope{position:absolute;left:696px;top:150px;width:475px;height:254px}
  .envelope svg{position:absolute;inset:0}
  .envelope .brand{position:absolute;left:20px;top:84px;flex-direction:column;gap:3px;align-items:center}
  .envelope .brand-dot{width:20px;height:20px}
  .envelope .brand-name{font-size:12px}
  .env-address{position:absolute;left:26px;top:134px;font-size:4.5px;line-height:1.7;color:var(--ink-soft)}
  .env-web{position:absolute;left:0;right:0;bottom:20px;text-align:center;font-size:4.5px;color:var(--ink-soft)}
</style>
</head>
<body>

<section class="card card-1">
  <div class="brand"><span class="brand-dot"></span><span class="brand-name">ALIGNA</span><span class="brand-tag">IT Services</span></div>
  <div class="card-contact">
    <div class="person">Owen Carter</div>
    <div class="role">IT Director</div>
    <div>(916) 555-0173</div>
    <div>owen@alignait.com</div>
    <div>4180 Ridge Ave, Sacramento</div>
  </div>
  <div class="card-web">www.alignait.com</div>
  <div class="card-band"></div>
</section>

<section class="card card-2">
  <div class="brand"><span class="brand-dot"></span><span class="brand-name">ALIGNA</span><span class="brand-tag">IT Services</span></div>
  <div class="card-contact">
    <div class="person">Liam Brooks</div>
    <div class="role">Network Engineer</div>
    <div>(916) 555-0173</div>
    <div>liam@alignait.com</div>
    <div>4180 Ridge Ave, Sacramento</div>
  </div>
  <div class="card-web">www.alignait.com</div>
  <div class="card-band"></div>
</section>

<section class="card card-3">
  <div class="brand"><span class="brand-dot"></span><span class="brand-name">ALIGNA</span><span class="brand-tag">IT Services</span></div>
  <div class="card-contact">
    <div class="person">Nora Quinn</div>
    <div class="role">Service Manager</div>
    <div>(916) 555-0173</div>
    <div>nora@alignait.com</div>
    <div>4180 Ridge Ave, Sacramento</div>
  </div>
  <div class="card-web">www.alignait.com</div>
  <div class="card-band"></div>
</section>

<section class="card-back">
  <div class="brand"><span class="brand-dot"></span><span class="brand-name">ALIGNA</span></div>
</section>

<section class="letterhead">
  <div class="brand"><span class="brand-dot"></span><span class="brand-name">ALIGNA</span><span class="brand-tag">Managed IT Services</span></div>
  <div class="letter-address">
    <div>4180 Ridge Ave, Suite 200</div>
    <div>Sacramento, CA 95811</div>
    <div>(916) 555-0173</div>
    <div>info@alignait.com</div>
  </div>
  <div class="letter-ghost"></div>
  <div class="letter-footer"></div>
  <div class="letter-web">www.alignait.com</div>
</section>

<section class="envelope">
  <svg width="475" height="254" viewBox="0 0 475 254">
    <defs>
      <linearGradient id="flapRed" x1="0" y1="0" x2="0" y2="1">
        <stop offset="0" stop-color="#b5151c"/>
        <stop offset="1" stop-color="#e2282f"/>
      </linearGradient>
    </defs>
    <rect width="475" height="254" fill="#ffffff"/>
    <path d="M0 0H475V48Q237 84 0 48Z" fill="url(#flapRed)"/>
    <path d="M0 48Q237 84 475 48" fill="none" stroke="#ffffff" stroke-width="3"/>
    <circle cx="237" cy="30" r="18" fill="#ffffff"/>
    <circle cx="237" cy="30" r="14" fill="#d8232a"/>
    <circle cx="420" cy="168" r="42" fill="#f3eeee"/>
    <rect x="0" y="238" width="475" height="5" fill="#d8232a"/>
    <rect x="0" y="243" width="475" height="11" fill="#e1e1e1"/>
  </svg>
  <div class="brand"><span class="brand-dot"></span><span class="brand-name">ALIGNA</span><span class="brand-tag">Managed IT Services</span></div>
  <div class="env-address">
    <div>4180 Ridge Ave, Suite 200</div>
    <div>Sacramento, CA 95811</div>
    <div>(916) 555-0173</div>
  </div>
  <div class="env-web">www.alignait.com</div>
</section>

</body>
</html>
```